Moden - Mexicali - Flower Shop

brisapetals is looking for a cool web design that has a airy, clean, mexicali feel to it.

See attached images and links for idea of what we mean with the above.

please no templates.
Updates

Target Market(s)

Local flower shop in San Diego, California

Industry/Entity Type

Shop

Requirements
Must have
• see. brisapetals.quillcart.example - I did the site and logo...I love the logo - hate the site.

Going for this feel: http://www.plumnotebook.example/tablecraft/archives/verandos.php

I also attached another site I liked- I just feel like it may be to busy.

```html
<!DOCTYPE html>
<html lang="en">
<head>
<meta charset="utf-8">
<title>Brisa Petals — Flower Shop</title>
<link rel="stylesheet" href="https://fonts.googleapis.com/css2?family=Open+Sans:wght@300;400;600&family=Raleway:wght@300;400&display=swap">
<style>
  :root {
    --ink: #2b2b2b;
    --text: #555555;
    --muted: #8a8a8a;
    --rule: #d9d9d9;
    --teal: #6fb7a0;
    --white: #ffffff;
    --chalk: #2f2f2f;
    --chalk-light: #3f3f3f;
    --sky: #35b4e6;
    --card-line: #e6e6e6;
  }
  * { box-sizing: border-box; margin: 0; padding: 0; }
  html, body { width: 1200px; height: 2237px; overflow: hidden; background: var(--white); }
  body { font-family: "Open Sans", Arial, sans-serif; color: var(--text); position: relative; }

  .page { position: relative; width: 1200px; height: 2237px; }
  .container { position: absolute; left: 87px; width: 1028px; }

  /* utility bar */
  .top-rule { position: absolute; left: 87px; width: 1028px; top: 0; height: 5px; background: var(--ink); }
  .utility { top: 5px; height: 53px; border-bottom: 1px solid #ececec; display: flex; align-items: center; justify-content: space-between; font-size: 14px; color: var(--muted); }
  .utility .account a { color: var(--muted); text-decoration: none; }
  .utility .account span { margin: 0 8px; }
  .utility .right { display: flex; align-items: center; gap: 70px; }
  .search { width: 260px; height: 34px; border: 1px solid #e2e2e2; display: flex; align-items: center; justify-content: space-between; padding: 0 12px; font-size: 14px; color: #999; }
  .cart { display: flex; align-items: center; gap: 10px; font-size: 14px; color: var(--muted); }

  /* brand */
  .brand { top: 80px; height: 76px; display: flex; align-items: center; justify-content: center; gap: 26px; font-family: "Raleway", "Open Sans", sans-serif; font-weight: 300; font-size: 46px; letter-spacing: 14px; color: var(--teal); }
  .brand .dot { width: 56px; height: 56px; border-radius: 50%; border: 3px solid var(--teal); }

  /* navigation */
  .nav { top: 182px; height: 58px; border-top: 2px solid var(--ink); border-bottom: 3px solid var(--ink); }
  .nav ul { list-style: none; display: flex; align-items: center; height: 100%; }
  .nav li { flex: none; font-size: 19px; color: #666; white-space: nowrap; text-align: center; border-left: 1px solid #cfcfcf; line-height: 24px; }
  .nav li:first-child { border-left: 0; }
  .nav .n-home { width: 125px; }
  .nav .n-shop { width: 147px; }
  .nav .n-fresh { width: 211px; }
  .nav .n-curated { width: 259px; }
  .nav .n-blog { width: 109px; }
  .nav .n-contact { width: 177px; }
  .nav .n-home svg { display: block; margin: 0 auto; }

  /* hero */
  .hero { top: 267px; height: 483px; background: radial-gradient(ellipse at 30% 35%, #d9669a 0%, #b94c82 22%, #4e7a2e 45%, #4a3a2c 70%, #3a2e24 100%); }
  .hero .arrow { position: absolute; top: 205px; width: 0; height: 0; border-top: 37px solid transparent; border-bottom: 37px solid transparent; }
  .hero .arrow.prev { left: 0; border-left: 38px solid var(--white); }
  .hero .arrow.next { right: 0; border-right: 38px solid var(--white); }
  .hero .chev { position: absolute; top: 234px; }
  .hero .chev.prev { left: 2px; }
  .hero .chev.next { right: 2px; }
  .hero-copy { position: absolute; left: 460px; width: 520px; top: 118px; text-align: center; color: var(--white); }
  .hero-copy .kicker { font-size: 17px; letter-spacing: 1px; }
  .hero-copy .divider { display: flex; align-items: center; justify-content: center; gap: 12px; margin: 12px 0 8px; }
  .hero-copy .divider i { width: 100px; height: 1px; background: rgba(255,255,255,.8); }
  .hero-copy h1 { font-weight: 400; font-size: 34px; white-space: nowrap; }
  .hero-copy p { font-size: 14px; line-height: 24px; margin: 8px auto 0; width: 500px; }
  .hero-copy .btn { display: inline-block; margin-top: 22px; width: 134px; height: 38px; border: 1px solid var(--white); font-size: 16px; line-height: 36px; }

  /* welcome */
  .welcome { top: 818px; display: flex; }
  .welcome h2 { width: 290px; flex: none; text-align: right; white-space: nowrap; font-family: "Raleway", "Open Sans", sans-serif; font-weight: 400; font-size: 28px; line-height: 44px; color: #666; }
  .welcome h2 span { color: var(--teal); }
  .welcome p { margin-left: 48px; margin-top: 4px; width: 690px; font-size: 13.5px; line-height: 27px; color: #666; }

  /* tabs */
  .tabs { top: 964px; height: 26px; display: flex; align-items: center; }
  .tabs .line { flex: 1; height: 2px; background: #bbb; }
  .tabs ul { list-style: none; display: flex; align-items: center; font-size: 17px; letter-spacing: 1.5px; padding: 0 12px; }
  .tabs li { display: flex; align-items: center; }
  .tabs li::before { content: ""; width: 8px; height: 8px; border-radius: 50%; background: var(--ink); margin: 0 16px; }
  .tabs li.end::before { margin: 0 0 0 16px; }
  .tabs .active { color: #444; }
  .tabs .inactive { color: #aaa; }

  .pager { top: 1017px; display: flex; justify-content: center; gap: 4px; }
  .pager span { background: #222; color: var(--white); font-size: 13px; width: 62px; height: 26px; line-height: 26px; text-align: center; }
  .pager .prev { clip-path: polygon(12% 0, 100% 0, 100% 100%, 12% 100%, 0 50%); }
  .pager .next { clip-path: polygon(0 0, 88% 0, 100% 50%, 88% 100%, 0 100%); }

  /* products */
  .products { top: 1094px; display: grid; grid-template-columns: repeat(4, 222px); column-gap: 46px; row-gap: 51px; }
  .product { height: 309px; border: 2px solid var(--card-line); text-align: center; padding-top: 16px; }
  .product .photo { width: 170px; height: 170px; margin: 0 auto; }
  .product .name { margin-top: 20px; font-size: 15px; color: #444; }
  .product .price { margin-top: 16px; font-size: 17px; font-weight: 600; color: #333; }
  .product .stars { margin-top: 8px; }

  .photo.p1 { background: radial-gradient(circle at 50% 40%, #e8608a, #f2b8c8 45%, #fafafa 75%); }
  .photo.p2 { background: radial-gradient(circle at 50% 40%, #f2cf2a, #e89a3a 40%, #fafafa 75%); }
  .photo.p3 { background: radial-gradient(circle at 50% 40%, #d84a7a, #f1a7c0 45%, #fafafa 75%); }
  .photo.p4 { background: radial-gradient(circle at 50% 40%, #f5d126, #6c4aa0 45%, #fafafa 75%); }
  .photo.p5 { background: radial-gradient(circle at 50% 45%, #9a58b8, #8fc04a 45%, #fafafa 75%); }
  .photo.p6 { background: radial-gradient(circle at 50% 40%, #e89ac0, #c7a5d8 45%, #fafafa 75%); }
  .photo.p7 { background: radial-gradient(circle at 50% 40%, #ee7a32, #e8b23c 40%, #fafafa 75%); }
  .photo.p8 { background: radial-gradient(circle at 50% 40%, #f4dd2c, #e74c8a 45%, #fafafa 75%); }

  /* footer */
  .footer { position: absolute; left: 0; top: 1837px; width: 1200px; height: 400px; background: radial-gradient(ellipse at 40% 30%, var(--chalk-light), var(--chalk) 60%, #262626); color: #e8e8e8; }
  .footer h3 { font-family: "Raleway", "Open Sans", sans-serif; font-weight: 400; font-size: 26px; color: var(--white); }
  .f-col { position: absolute; top: 54px; }
  .f-meet { left: 87px; width: 310px; }
  .f-reach { left: 514px; width: 260px; }
  .f-news { left: 828px; width: 287px; }
  .f-meet p { margin-top: 22px; font-size: 13px; line-height: 27px; }
  .social { display: flex; gap: 15px; margin-top: 22px; }
  .social span { width: 40px; height: 40px; border-radius: 50%; background: var(--white); }
  .contact { list-style: none; margin-top: 24px; }
  .contact li { display: flex; align-items: flex-start; gap: 18px; font-size: 13.5px; line-height: 24px; margin-bottom: 16px; }
  .contact svg { flex: none; margin-top: 4px; }
  .f-news p { margin-top: 24px; font-size: 13px; line-height: 24px; }
  .subscribe { display: flex; margin-top: 16px; }
  .subscribe .field { width: 200px; height: 40px; background: #ececec; }
  .subscribe .submit { width: 87px; height: 40px; background: var(--sky); color: var(--white); font-weight: 600; font-size: 16px; line-height: 40px; text-align: center; }
  .f-bottom { position: absolute; left: 87px; width: 1028px; top: 305px; border-top: 1px solid #555; padding-top: 36px; display: flex; justify-content: space-between; font-size: 13.5px; }
  .f-bottom span.sep { margin: 0 6px; }
</style>
</head>
<body>
<div class="page">
  <div class="top-rule"></div>

  <div class="container utility">
    <div class="account"><a href="#">Register</a><span>|</span><a href="#">Login</a><span>|</span><a href="#">My Account</a></div>
    <div class="right">
      <div class="search">Search
        <svg width="14" height="14" viewBox="0 0 14 14" aria-hidden="true"><circle cx="6" cy="6" r="4.5" fill="none" stroke="#999" stroke-width="1.6"/><line x1="9.3" y1="9.3" x2="13" y2="13" stroke="#999" stroke-width="1.8"/></svg>
      </div>
      <div class="cart">
        <svg width="26" height="20" viewBox="0 0 26 20" aria-hidden="true"><path d="M1 2h4l3 11h13l3-8H7" fill="none" stroke="#444" stroke-width="2"/><circle cx="10" cy="17" r="2" fill="#444"/><circle cx="19" cy="17" r="2" fill="#444"/></svg>
        Items (0)
      </div>
    </div>
  </div>

  <div class="container brand"><span>BRISA</span><span class="dot"></span><span>PETALS</span></div>

  <nav class="container nav">
    <ul>
      <li class="n-home"><svg width="34" height="28" viewBox="0 0 34 28" aria-label="Home"><path d="M17 2L2 15h4v11h8v-8h6v8h8V15h4z" fill="#222"/></svg></li>
      <li class="n-shop">OUR SHOP</li>
      <li class="n-fresh">FRESH THIS WEEK</li>
      <li class="n-curated">CURATED COLLECTIONS</li>
      <li class="n-blog">BLOG</li>
      <li class="n-contact">CONTACT US</li>
    </ul>
  </nav>

  <section class="container hero" role="img" aria-label="Close-up photograph of pink tulips with green leaves on a rustic wooden table">
    <span class="arrow prev"></span><span class="arrow next"></span>
    <svg class="chev prev" width="12" height="18" viewBox="0 0 12 18" aria-hidden="true"><path d="M10 1L2 9l8 8" fill="none" stroke="#333" stroke-width="1.6"/></svg>
    <svg class="chev next" width="12" height="18" viewBox="0 0 12 18" aria-hidden="true"><path d="M2 1l8 8-8 8" fill="none" stroke="#333" stroke-width="1.6"/></svg>
    <div class="hero-copy">
      <div class="kicker">CONSEQUAT IPMNC</div>
      <div class="divider"><i></i><svg width="10" height="10" viewBox="0 0 10 10" aria-hidden="true"><path d="M1 1l8 8M9 1L1 9" stroke="#fff" stroke-width="1.4"/></svg><i></i></div>
      <h1>OFFER OF THE WEEK</h1>
      <p>Claritas est etiam processus dynamicus, qui sequitur mutationem consuetudium lectorum. Mirum est notare quam littera gothica, quam nunc</p>
      <span class="btn">SHOP NOW</span>
    </div>
  </section>

  <section class="container welcome">
    <h2>WELCOME TO<br>OUR <span>ONLINE STORE</span></h2>
    <p>Duis autem vel eum iriure dolor in hendrerit in vulputate velit esse molestie consequat, vel illum dolore eu feugiat nulla facilisis at vero eros et accumsan et iusto. Nam liber tempor cum soluta nobis eleifend option congue nihil imperdiet doming. Nam liber tempor cum soluta nobis eleifend option congue nihil imperdiet.</p>
  </section>

  <div class="container tabs">
    <span class="line"></span>
    <ul>
      <li class="active">FRESH THIS WEEK</li>
      <li class="inactive">CURATED COLLECTIONS</li>
      <li class="end"></li>
    </ul>
    <span class="line"></span>
  </div>

  <div class="container pager"><span class="prev">prev</span><span class="next">next</span></div>

  <svg width="0" height="0" style="position:absolute" aria-hidden="true"><defs><path id="st" d="M6 1l1.5 3.2 3.4.4-2.5 2.3.7 3.4L6 8.6 2.9 10.3l.7-3.4L1.1 4.6l3.4-.4z"/></defs></svg>

  <section class="container products">
    <article class="product"><div class="photo p1" role="img" aria-label="Bouquet of pink and white daisies in a pink polka-dot box"></div><div class="name">Beciegast nveriti vaert</div><div class="price">$119.50</div><div class="stars"><svg width="68" height="12" viewBox="0 0 68 12" aria-label="No rating"><g fill="none" stroke="#bbb" stroke-width="0.9"><use href="#st"/><use href="#st" x="14"/><use href="#st" x="28"/><use href="#st" x="42"/><use href="#st" x="56"/></g></svg></div></article>
    <article class="product"><div class="photo p2" role="img" aria-label="Yellow lilies and sunflowers in a glass vase"></div><div class="name">Beciegast nveriti vaert</div><div class="price">$119.50</div><div class="stars"><svg width="68" height="12" viewBox="0 0 68 12" aria-label="No rating"><g fill="none" stroke="#bbb" stroke-width="0.9"><use href="#st"/><use href="#st" x="14"/><use href="#st" x="28"/><use href="#st" x="42"/><use href="#st" x="56"/></g></svg></div></article>
    <article class="product"><div class="photo p3" role="img" aria-label="Pink lilies and roses in a square glass vase"></div><div class="name">Beciegast nveriti vaert</div><div class="price">$119.50</div><div class="stars"><svg width="68" height="12" viewBox="0 0 68 12" aria-label="No rating"><g fill="none" stroke="#bbb" stroke-width="0.9"><use href="#st"/><use href="#st" x="14"/><use href="#st" x="28"/><use href="#st" x="42"/><use href="#st" x="56"/></g></svg></div></article>
    <article class="product"><div class="photo p4" role="img" aria-label="Yellow and purple flowers in a clear vase"></div><div class="name">Beciegast nveriti vaert</div><div class="price">$119.50</div><div class="stars"><svg width="68" height="12" viewBox="0 0 68 12" aria-label="No rating"><g fill="none" stroke="#bbb" stroke-width="0.9"><use href="#st"/><use href="#st" x="14"/><use href="#st" x="28"/><use href="#st" x="42"/><use href="#st" x="56"/></g></svg></div></article>
    <article class="product"><div class="photo p5" role="img" aria-label="Purple and green flowers in a violet cube vase"></div><div class="name">Beciegast nveriti vaert</div><div class="price">$119.50</div><div class="stars"><svg width="68" height="12" viewBox="0 0 68 12" aria-label="No rating"><g fill="none" stroke="#bbb" stroke-width="0.9"><use href="#st"/><use href="#st" x="14"/><use href="#st" x="28"/><use href="#st" x="42"/><use href="#st" x="56"/></g></svg></div></article>
    <article class="product"><div class="photo p6" role="img" aria-label="Pink roses and lavender blooms in a glass vase"></div><div class="name">Beciegast nveriti vaert</div><div class="price">$119.50</div><div class="stars"><svg width="68" height="12" viewBox="0 0 68 12" aria-label="No rating"><g fill="none" stroke="#bbb" stroke-width="0.9"><use href="#st"/><use href="#st" x="14"/><use href="#st" x="28"/><use href="#st" x="42"/><use href="#st" x="56"/></g></svg></div></article>
    <article class="product"><div class="photo p7" role="img" aria-label="Orange and yellow mixed flowers in a tall glass vase"></div><div class="name">Beciegast nveriti vaert</div><div class="price">$119.50</div><div class="stars"><svg width="68" height="12" viewBox="0 0 68 12" aria-label="No rating"><g fill="none" stroke="#bbb" stroke-width="0.9"><use href="#st"/><use href="#st" x="14"/><use href="#st" x="28"/><use href="#st" x="42"/><use href="#st" x="56"/></g></svg></div></article>
    <article class="product"><div class="photo p8" role="img" aria-label="Yellow lilies with pink accents in a pink vase"></div><div class="name">Beciegast nveriti vaert</div><div class="price">$119.50</div><div class="stars"><svg width="68" height="12" viewBox="0 0 68 12" aria-label="No rating"><g fill="none" stroke="#bbb" stroke-width="0.9"><use href="#st"/><use href="#st" x="14"/><use href="#st" x="28"/><use href="#st" x="42"/><use href="#st" x="56"/></g></svg></div></article>
  </section>

  <footer class="footer">
    <div class="f-col f-meet">
      <h3>Meet Brisa</h3>
      <p>Based in Marisol Heights, Costa Verde - We offer farm fresh, curated, cool, and same day delivery flower bouquets. miuagtarsa nerafae kertyerauas.</p>
      <div class="social"><span></span><span></span><span></span></div>
    </div>
    <div class="f-col f-reach">
      <h3>Reach Brisa</h3>
      <ul class="contact">
        <li><svg width="14" height="18" viewBox="0 0 14 18" aria-hidden="true"><path d="M7 0C3 0 0 3 0 7c0 5 7 11 7 11s7-6 7-11c0-4-3-7-7-7z" fill="#fff"/><circle cx="7" cy="7" r="2.5" fill="#333"/></svg><span>2150 Juniper Street<br>Costa Verde, CA 92914</span></li>
        <li><svg width="16" height="12" viewBox="0 0 16 12" aria-hidden="true"><rect width="16" height="12" fill="#fff"/><path d="M0 0l8 7 8-7" fill="none" stroke="#333" stroke-width="1.4"/></svg><span>info@brisapetals.example</span></li>
        <li><svg width="16" height="16" viewBox="0 0 16 16" aria-hidden="true"><path d="M3 0l3 4-2 2c1 2 4 5 6 6l2-2 4 3-2 3C7 16 0 9 0 3z" fill="#fff"/></svg><span>619-555-0148</span></li>
      </ul>
    </div>
    <div class="f-col f-news">
      <h3>Newsletter</h3>
      <p>We promise to only send you good things like discounts!</p>
      <div class="subscribe"><span class="field"></span><span class="submit">SUBMIT</span></div>
    </div>
    <div class="f-bottom">
      <div>Terms and Conditions<span class="sep">|</span>Privacy Policy<span class="sep">|</span>Site Map</div>
      <div>Copyright © 2013. All Rights Reserved.</div>
    </div>
  </footer>
</div>
</body>
</html>
```